Card design for Heating and Cooling company

this is for a heating and cooling company we recently updated our logo and need to update our cards. We attached our logo so you can incorporate it into the card. We specialize in residential and commercial furnace and air condition repairs. Have been in business since 2014.

Phone number 555.284.9137

We need the following phrases
:Repairs, Installations, and maintenance
:Quality work at reasonable prices
:residential/commercial
:Licensed &Insured
:Email Pinegrovehvac47@mailbox-example.com
Name: Teodor K (Ted)
Also on back side I would like my logo with wording :Thank you for your business and refferal

Industry/Entity Type

Hvac

Contact Information for Business Card

:residential/commercial
:Licensed & Insured
Name: Teodor K (Ted)
Number:555.284.9136

Requirements
Must have
• Blue and red colors
Nice to have
• Maybe a pic of a furnace or air conditioner

```html
<!DOCTYPE html>
<html lang="en">
<head>
<meta charset="utf-8">
<title>Pinegrove Heating &amp; Cooling – Business Cards</title>
<link href="https://fonts.googleapis.com/css2?family=Roboto:wght@400;500;700&display=swap" rel="stylesheet">
<style>
  :root {
    --page-bg: #e4e6e8;
    --card-light: #e6f1f5;
    --card-mid: #c9e0ea;
    --brand-blue: #2fa6df;
    --brand-red: #e52421;
    --ink: #1d1f22;
    --white: #ffffff;
    --unit-light: #fbfcfd;
    --unit-shade: #d6dde2;
  }
  * { box-sizing: border-box; margin: 0; padding: 0; }
  html, body { width: 1200px; height: 930px; overflow: hidden; }
  body {
    background: var(--page-bg);
    font-family: "Roboto", Arial, sans-serif;
    color: var(--ink);
    position: relative;
  }
  .card {
    position: absolute;
    left: 250px;
    width: 700px;
    height: 400px;
    border-radius: 22px;
    overflow: hidden;
    background: linear-gradient(160deg, var(--card-light) 0%, var(--card-mid) 100%);
    box-shadow: 0 6px 18px rgba(0,0,0,0.18);
  }
  .card--front { top: 50px; }
  .card--back { top: 480px; }

  .product-photo {
    position: absolute;
    border-radius: 14px;
    background: linear-gradient(180deg, var(--unit-light) 0%, var(--unit-light) 62%, var(--unit-shade) 80%, #9fc6dc 100%);
  }
  .card--front .product-photo { left: 40px; top: 70px; width: 470px; height: 175px; }
  .card--back .product-photo { left: 40px; top: 130px; width: 420px; height: 160px; }

  .airflow {
    position: absolute;
    left: 420px; top: 40px; width: 280px; height: 200px;
    border-radius: 0 22px 0 0;
    background: linear-gradient(200deg, rgba(47,166,223,0) 10%, rgba(47,166,223,0.4) 60%, rgba(47,166,223,0) 100%);
  }

  .brand {
    position: absolute;
    display: flex;
    align-items: center;
    gap: 10px;
  }
  .card--front .brand { left: 130px; top: 140px; }
  .card--back .brand { left: 70px; top: 180px; }
  .brand__dot {
    width: 20px; height: 20px; border-radius: 50%;
    background: var(--brand-blue);
  }
  .brand__name {
    font-weight: 700;
    font-size: 22px;
    color: var(--ink);
    letter-spacing: 0.3px;
  }
  .card--front .brand__name { font-size: 24px; }

  .services {
    position: absolute;
    right: 40px; top: 262px;
    text-align: right;
    font-size: 17px;
    line-height: 1.3;
    color: var(--ink);
  }

  .waves { position: absolute; inset: 0; width: 700px; height: 400px; }

  .holder {
    position: absolute;
    right: 40px; top: 30px;
    text-align: right;
  }
  .holder__name {
    font-size: 26px;
    font-weight: 500;
    color: var(--brand-red);
  }
  .holder__role { font-size: 16px; margin-top: 2px; }

  .contacts {
    position: absolute;
    right: 34px; top: 215px;
    list-style: none;
    text-align: right;
    color: var(--white);
    font-size: 14px;
    line-height: 1.55;
  }
  .contacts li { display: flex; justify-content: flex-end; align-items: center; gap: 8px; }
  .contacts svg { width: 12px; height: 12px; flex: none; }
</style>
</head>
<body>

<section class="card card--front">
  <div class="product-photo" role="img" aria-label="Photo of a white wall-mounted air conditioner unit"></div>
  <div class="airflow" role="img" aria-label="Soft blue cool-air flow graphic"></div>
  <div class="brand">
    <span class="brand__dot"></span>
    <span class="brand__name">Pinegrove Heating &amp; Cooling</span>
  </div>
  <p class="services">
    Repairs, Installations, and maintenance<br>
    Quality work at reasonable prices<br>
    residential/commercial | Licensed &amp; Insured
  </p>
</section>

<section class="card card--back">
  <div class="product-photo" role="img" aria-label="Photo of a white wall-mounted air conditioner unit"></div>
  <svg class="waves" viewBox="0 0 700 400" aria-hidden="true">
    <path d="M700 70 C560 70 480 190 420 240 C360 290 220 300 0 310 L0 400 L700 400 Z" fill="var(--brand-blue)"/>
    <path d="M700 58 C555 58 475 180 415 232 C470 185 560 80 700 78 Z" fill="var(--white)" opacity="0.7"/>
    <path d="M0 272 C200 292 340 292 412 244 C350 300 200 316 0 304 Z" fill="var(--brand-red)"/>
  </svg>
  <div class="brand">
    <span class="brand__dot"></span>
    <span class="brand__name">Pinegrove Heating &amp; Cooling</span>
  </div>
  <div class="holder">
    <p class="holder__name">TEODOR K (TED)</p>
    <p class="holder__role">Director</p>
  </div>
  <ul class="contacts">
    <li>555.284.9137
      <svg viewBox="0 0 16 16"><path d="M3 1l3 3-1.5 2a9 9 0 0 0 5.5 5.5L12 10l3 3-2 2C7 15 1 9 1 3z" fill="currentColor"/></svg>
    </li>
    <li>555.284.9136
      <svg viewBox="0 0 16 16"><rect x="4" y="1" width="8" height="14" rx="1.5" fill="none" stroke="currentColor" stroke-width="1.6"/></svg>
    </li>
    <li>Pinegrovehvac47@mailbox-example.com
      <svg viewBox="0 0 16 16"><rect x="1" y="3" width="14" height="10" fill="none" stroke="currentColor" stroke-width="1.5"/><path d="M1 3l7 6 7-6" fill="none" stroke="currentColor" stroke-width="1.5"/></svg>
    </li>
    <li>www.pinegrovehvac-example.com
      <svg viewBox="0 0 16 16"><circle cx="8" cy="8" r="6.5" fill="none" stroke="currentColor" stroke-width="1.4"/><path d="M1.5 8h13M8 1.5c-3 3.5-3 9.5 0 13M8 1.5c3 3.5 3 9.5 0 13" fill="none" stroke="currentColor" stroke-width="1.2"/></svg>
    </li>
  </ul>
</section>

</body>
</html>
```